Design revision of an existing Executive Summary

Our company velnova is specialized in the field of performance engineering (load and performance testing as well as application performance monitoring). We are looking for a designer who could graphically "spice up" our current executive summary about our company velnova (www.velnova-ops.com). Maybe it would be possible to incorporate a pic of our website (e.g. https://www.velnova-ops.com/en/services/performance/) into this newly designed executive summary.

Attached you will find the current executive summary which should not change textually. It should just look fresher and more modern. Ideally, a visually appealing first / title page would precede the text.

```html
<!DOCTYPE html>
<html lang="en">
<head>
<meta charset="utf-8">
<title>velnova – Executive Summary</title>
<link href="https://fonts.googleapis.com/css2?family=Montserrat:wght@300;600;800&family=Open+Sans:wght@400;600&display=swap" rel="stylesheet">
<style>
  :root{
    --navy:#1d3a7a;
    --navy-deep:#1a2f6b;
    --blue:#1565c0;
    --sky:#3fa9f5;
    --ice:#d3e8f8;
    --paper:#f5f6fa;
    --ink:#1d2d5a;
    --white:#ffffff;
    --stage:#d9dbe0;
  }
  *{box-sizing:border-box;margin:0;padding:0}
  html,body{width:1200px;height:800px;overflow:hidden;background:var(--stage)}
  body{font-family:"Open Sans",sans-serif;color:var(--ink)}
  .summary{position:absolute;left:300px;top:10px;width:600px;height:780px;background:var(--paper);overflow:hidden;box-shadow:0 4px 18px rgba(0,0,0,.18)}
  .abs{position:absolute}
  .brand{left:34px;top:76px;font-family:"Montserrat",sans-serif;font-weight:300;font-size:50px;letter-spacing:1px;color:var(--navy)}
  .hero-photo{left:250px;top:0;width:350px;height:200px;clip-path:polygon(0 0,100% 0,100% 100%,30% 100%);background:linear-gradient(135deg,#8c9bb0 0%,#c9d2de 45%,#e8ecf2 100%)}
  .hero-edge{left:238px;top:0;width:120px;height:200px;clip-path:polygon(0 0,8% 0,100% 100%,92% 100%);background:var(--blue)}
  .ice-band{left:0;top:190px;width:600px;height:222px;background:var(--ice)}
  .title-band{left:0;top:150px;width:340px;height:120px;background:var(--navy);clip-path:polygon(0 0,84% 0,100% 100%,0 100%)}
  .headline{left:34px;top:162px;font-family:"Montserrat",sans-serif;font-weight:800;font-size:27px;line-height:1;color:var(--sky);letter-spacing:.5px}
  .tagline{left:34px;top:226px;font-family:"Montserrat",sans-serif;font-weight:600;font-size:12.5px;line-height:1.3;color:var(--white)}
  h2{font-family:"Montserrat",sans-serif;font-weight:800;font-size:15px;color:var(--navy);letter-spacing:.3px;border-bottom:2px solid currentColor;display:inline-block;padding-bottom:1px;margin-bottom:6px}
  p{font-size:9.3px;line-height:1.5}
  .who{left:34px;top:280px;width:536px}
  .who p+p{margin-top:5px}
  .services{left:300px;top:412px;width:300px;height:308px;background:var(--blue);color:var(--white);padding:11px 22px 0 22px}
  .services h2{color:var(--white);margin-bottom:2px}
  .service{display:flex;gap:12px;margin-top:6px}
  .service svg{flex:0 0 40px}
  .service h3{font-family:"Montserrat",sans-serif;font-weight:800;font-size:10.5px;color:var(--sky);margin-bottom:1px}
  .service p{font-size:8.8px;line-height:1.4}
  .team{left:34px;top:422px;width:248px}
  .customers{left:34px;top:610px;width:250px}
  .clients{display:grid;grid-template-columns:1fr 1fr;gap:6px 12px;margin-top:2px;font-weight:600;font-size:13px}
  .client{display:flex;align-items:center;gap:5px}
  .client i{display:inline-block;width:10px;height:10px}
  .footer{left:0;top:720px;width:600px;height:60px;background:var(--navy-deep);color:var(--white);display:grid;grid-template-columns:repeat(3,auto);gap:6px 20px;align-content:center;padding:0 26px;font-size:9px}
  .contact{display:flex;align-items:center;gap:6px}
  .contact svg{flex:0 0 14px}
</style>
</head>
<body>
<main class="summary">
  <div class="abs ice-band"></div>
  <div class="abs hero-edge"></div>
  <div class="abs hero-photo" role="img" aria-label="Photo of a team meeting around a table with a presenter at a screen"></div>
  <div class="abs title-band"></div>
  <div class="abs brand">velnova</div>
  <div class="abs headline">PERFORMANCE<br>MATTERS.</div>
  <div class="abs tagline">Your service provider to ensure<br>application performance.</div>

  <section class="abs who">
    <h2>WHO WE ARE?</h2>
    <p>velnova is the go-to-company in the very specialized area of performance engineering. Whether microservices in the cloud or legacy on-premise: We will show you the added value of load and performance tests, performance tuning or monitoring solutions.</p>
    <p>In the area of application performance monitoring, we like to work with the enterprise solution from industry leader Tracewell. velnova is Tracewell Premier Partner and therefore amongst an exclusive group of companies in the EMEA region specialized in Tracewell.</p>
  </section>

  <section class="abs team">
    <h2>ABOUT OUR TEAM</h2>
    <p>Our performance engineers guide our customers through the whole process of performance testing by providing best practices for test design and test strategies, setting up infrastructure, carrying out performance tests as well as preparing the reporting. If required, our performance engineers go beyond reporting by identifying the actual bottlenecks and even performing code reviews. As we offer to play such an active role in fixing performance defects, all our consultants are well-skilled software engineers.</p>
  </section>

  <section class="abs customers">
    <h2>VALUED CUSTOMERS</h2>
    <div class="clients">
      <span class="client" style="color:#d32f2f">Kestrel IT</span>
      <span class="client" style="color:#1d3a7a"><i style="background:#1d3a7a"></i>Norvia</span>
      <span class="client" style="color:#e53935">Baumhof</span>
      <span class="client" style="color:#0d8a8a"><i style="background:#0d8a8a"></i>Cityline IT</span>
      <span class="client" style="color:#c62828">Chamberly</span>
      <span class="client" style="color:#1b8a3e"><i style="background:#1b8a3e"></i>Gemeindenet</span>
    </div>
  </section>

  <section class="abs services">
    <h2>OUR SERVICES</h2>
    <div class="service">
      <svg width="40" height="40" viewBox="0 0 40 40"><circle cx="20" cy="20" r="18" fill="none" stroke="#fff" stroke-width="2"/><path d="M10 25a10 10 0 1 1 20 0" fill="none" stroke="#fff" stroke-width="2"/><path d="M20 25l5-8" stroke="#fff" stroke-width="2"/></svg>
      <div><h3>Load &amp; Performance Testing</h3><p>An often-neglected necessity to ensure the speed, stability and reliability of your IT applications and digital services. If you expect many users rushing in on your digital roads, performance tests are required to provide the best experience for your customers.</p></div>
    </div>
    <div class="service">
      <svg width="40" height="40" viewBox="0 0 40 40"><circle cx="20" cy="20" r="18" fill="none" stroke="#fff" stroke-width="2"/><rect x="12" y="11" width="13" height="16" fill="none" stroke="#fff" stroke-width="1.6"/><circle cx="23" cy="23" r="4" fill="none" stroke="#fff" stroke-width="1.6"/><path d="M26 26l4 4" stroke="#fff" stroke-width="1.8"/></svg>
      <div><h3>APM &amp; Observability</h3><p>Follow the experience of users &amp; pinpoint the root-cause of problems as fast as possible in case of an undesired event and get business insights like usage statistics &amp; conversion rates just along the way.</p></div>
    </div>
    <div class="service">
      <svg width="40" height="40" viewBox="0 0 40 40"><circle cx="20" cy="20" r="18" fill="none" stroke="#fff" stroke-width="2"/><rect x="11" y="12" width="18" height="12" fill="none" stroke="#fff" stroke-width="1.6"/><path d="M14 21l4-4 3 3 5-5M20 24v5M15 29h10" fill="none" stroke="#fff" stroke-width="1.6"/></svg>
      <div><h3>Trainings &amp; Workshops</h3><p>Enable your own performance testing team by learning innovative approaches such as the automation of quality gates and automate performance feedback or get started with the basic methodology training.</p></div>
    </div>
  </section>

  <footer class="abs footer">
    <span class="contact"><svg width="14" height="14" viewBox="0 0 14 14"><circle cx="7" cy="7" r="7" fill="#3fa9f5"/><path d="M4.5 3.5l1.5 0 .6 1.8-.9.7a5 5 0 0 0 2.3 2.3l.7-.9 1.8.6v1.5c-3.6.3-6.3-2.4-6-6z" fill="#fff"/></svg>(+43) 100 20 30 4050</span>
    <span class="contact"><svg width="14" height="14" viewBox="0 0 14 14"><circle cx="7" cy="7" r="7" fill="#3fa9f5"/><rect x="3.5" y="4.5" width="7" height="5" fill="none" stroke="#fff" stroke-width="1"/><path d="M3.5 4.5l3.5 3 3.5-3" fill="none" stroke="#fff" stroke-width="1"/></svg>office@velnova-ops.com</span>
    <span class="contact"><svg width="14" height="14" viewBox="0 0 14 14"><circle cx="7" cy="7" r="7" fill="#3fa9f5"/><circle cx="7" cy="7" r="3.6" fill="none" stroke="#fff" stroke-width="1"/><path d="M3.4 7h7.2M7 3.4v7.2" stroke="#fff" stroke-width=".8"/></svg>www.orbitline-demo.org</span>
    <span class="contact"><svg width="14" height="14" viewBox="0 0 14 14"><circle cx="7" cy="7" r="7" fill="#3fa9f5"/></svg>www.socialhub.example/company/velnova</span>
  </footer>
</main>
</body>
</html>
```